"VeltaMakings" Graphic Design Project

We are a new business creating bath/ body/beauty products. We need label designs for men "Plume for Men " and women- "Plume for Women" . Since the collection called Plume will be used for both- we'd like the labels to look similar but separating the gender look- maybe by a same color variation. Our bottles are amber in color , so we like the beiges, cream, and earthy warm tones - greens- brown-orange- yellow-colors. The labels are for 8 oz amber cosmo round bottles. The height is 7.32inches and the diameter is 1.85 inches.
Our starting line will be Plume for Men ( Silk Body Wash, Silk Body Lotion and Body Mist) and the same for Plume for Women.

Target Market(s)

Our target audience is between 30 to 60 years of age. Salons and private consumers.
I am including attached sample of what was started by me.

Industry/Entity Type

Business

Requirements
Must have
• We would like to incorporate the company name- VeltaMakings along with the name of the product- which will be Plume for Men or Plume for Women on each label.

On label with company name or somewhere on label we would like a tree to symbolize the beginning, but we are open to suggestions.

```html
<!DOCTYPE html>
<html lang="en">
<head>
<meta charset="utf-8">
<title>Plume for Men – Silk Body Wash Label</title>
<link rel="stylesheet" href="https://fonts.googleapis.com/css2?family=Josefin+Sans:wght@400;600&family=Cormorant+Garamond:ital,wght@1,500;1,600&family=Arimo:wght@400&family=Archivo+Narrow:ital@1&display=swap">
<style>
  :root {
    --rust: #a4482a;
    --tan: #dcab79;
    --cream: #f8efd9;
    --cream-text: #f8ead0;
    --ink: #1c120c;
    --cocoa: #3a1c10;
    --gold-dark: #8a5a1a;
    --gold: #d19a22;
    --gold-light: #fbf3e2;
    --bronze: #6e3a22;
  }
  * { margin: 0; padding: 0; box-sizing: border-box; }
  html, body { width: 1006px; height: 1200px; overflow: hidden; background: #ffffff; }
  .canvas { position: relative; width: 1006px; height: 1200px; }
  .label-art { position: absolute; inset: 0; }
  .text { position: absolute; }

  /* Front label */
  .brand-name {
    left: 75px; width: 345px; top: 92px; text-align: center;
    font-family: "Josefin Sans", sans-serif; font-weight: 600;
    font-size: 26px; letter-spacing: 1px; color: var(--ink);
  }
  .product-name {
    left: 75px; width: 345px; top: 588px; text-align: center;
    font-family: "Josefin Sans", sans-serif; font-weight: 600;
    font-size: 56px; letter-spacing: 2px; color: var(--cream-text);
  }
  .audience {
    left: 75px; width: 345px; top: 662px; text-align: center; padding-left: 60px;
    font-family: "Cormorant Garamond", serif; font-style: italic; font-weight: 500;
    font-size: 42px; color: var(--cocoa);
  }
  .product-type {
    left: 75px; width: 345px; top: 792px; text-align: center;
    font-family: "Josefin Sans", sans-serif; font-weight: 600;
    font-size: 31px; letter-spacing: 0; color: var(--cream-text);
  }
  .volume {
    left: 75px; width: 345px; top: 1070px; text-align: center;
    font-family: "Arimo", sans-serif; font-size: 17px; color: var(--ink);
  }

  /* Back label */
  .tagline {
    left: 600px; width: 314px; top: 138px; text-align: center;
    font-family: "Cormorant Garamond", serif; font-style: italic; font-weight: 500;
    font-size: 27px; line-height: 33px; color: var(--cocoa);
  }
  .directions {
    left: 612px; width: 290px; top: 398px;
    font-family: "Arimo", sans-serif; font-size: 19px; line-height: 23px; color: var(--ink);
  }
  .warnings {
    left: 600px; width: 314px; top: 490px; text-align: center;
    font-family: "Arimo", sans-serif; font-size: 16px; line-height: 19px; color: var(--ink);
  }
  .claim {
    left: 600px; width: 314px; top: 578px; text-align: center;
    font-family: "Arimo", sans-serif; font-size: 17px; color: var(--ink);
  }
  .ingredients {
    left: 604px; width: 316px; top: 632px;
    font-family: "Archivo Narrow", sans-serif; font-style: italic;
    font-size: 15.8px; line-height: 17.4px; color: var(--cocoa);
  }
  .ingredients strong { font-weight: 700; }
  .company {
    left: 600px; width: 314px; top: 898px; text-align: center;
    font-family: "Cormorant Garamond", serif; font-style: italic; font-weight: 600;
    font-size: 25px; line-height: 31px; color: var(--ink);
  }
  .address {
    left: 600px; width: 314px; top: 958px; text-align: center;
    font-family: "Arimo", sans-serif; font-size: 18px; color: var(--ink);
  }
  .shop {
    left: 600px; width: 314px; top: 1016px; text-align: center;
    font-family: "Arimo", sans-serif; font-size: 18px; line-height: 23px; color: var(--ink);
  }
</style>
</head>
<body>
<main class="canvas">
  <svg class="label-art" width="1006" height="1200" viewBox="0 0 1006 1200" xmlns="http://www.w3.org/2000/svg">
    <defs>
      <linearGradient id="gold-frame" x1="0" y1="0" x2="0" y2="1">
        <stop offset="0" stop-color="var(--gold-dark)"/>
        <stop offset="0.05" stop-color="var(--gold)"/>
        <stop offset="0.2" stop-color="var(--gold-light)"/>
        <stop offset="0.32" stop-color="#e2c48a"/>
        <stop offset="0.45" stop-color="var(--gold)"/>
        <stop offset="0.6" stop-color="#f3e2bd"/>
        <stop offset="0.75" stop-color="#c9932e"/>
        <stop offset="0.9" stop-color="#8e5a28"/>
        <stop offset="1" stop-color="var(--bronze)"/>
      </linearGradient>
      <linearGradient id="front-field" x1="0" y1="0" x2="1" y2="1">
        <stop offset="0" stop-color="var(--rust)"/>
        <stop offset="0.5" stop-color="#c07a50"/>
        <stop offset="1" stop-color="var(--tan)"/>
      </linearGradient>
      <radialGradient id="tree-pale" cx="0.4" cy="0.45" r="0.6">
        <stop offset="0" stop-color="#f6e6c6" stop-opacity="0.75"/>
        <stop offset="1" stop-color="#f6e6c6" stop-opacity="0"/>
      </radialGradient>
      <radialGradient id="tree-rust" cx="0.55" cy="0.5" r="0.6">
        <stop offset="0" stop-color="#b5643a" stop-opacity="0.7"/>
        <stop offset="1" stop-color="#b5643a" stop-opacity="0"/>
      </radialGradient>
      <radialGradient id="tree-sand" cx="0.5" cy="0.5" r="0.6">
        <stop offset="0" stop-color="#e8cf9c" stop-opacity="0.8"/>
        <stop offset="1" stop-color="#e8cf9c" stop-opacity="0"/>
      </radialGradient>
      <clipPath id="front-clip"><rect x="75" y="62" width="345" height="1078" rx="172"/></clipPath>
      <clipPath id="back-clip"><rect x="585" y="62" width="345" height="1072" rx="172"/></clipPath>
    </defs>

    <!-- Front label -->
    <rect x="45" y="30" width="405" height="1140" rx="202" fill="url(#gold-frame)"/>
    <rect x="75" y="62" width="345" height="1078" rx="172" fill="url(#front-field)"/>
    <g clip-path="url(#front-clip)">
      <rect x="60" y="140" width="300" height="410" fill="url(#tree-pale)" role="img" aria-label="Cream silhouette of a branching tree with maple-like leaves"/>
      <rect x="140" y="750" width="290" height="340" fill="url(#tree-rust)" role="img" aria-label="Rust-toned silhouette of a leafy tree branch"/>
    </g>

    <!-- Back label -->
    <rect x="555" y="30" width="405" height="1135" rx="202" fill="url(#gold-frame)"/>
    <rect x="585" y="62" width="345" height="1072" rx="172" fill="var(--cream)"/>
    <g clip-path="url(#back-clip)">
      <rect x="690" y="55" width="170" height="85" fill="url(#tree-sand)" role="img" aria-label="Faint sand-coloured sprig of leaves"/>
      <rect x="570" y="860" width="230" height="260" fill="url(#tree-sand)" role="img" aria-label="Faint sand-coloured tree branch silhouette"/>
    </g>
  </svg>

  <div class="text brand-name">VeltaMakings</div>
  <div class="text product-name">PLUME</div>
  <div class="text audience">for men</div>
  <div class="text product-type">SILK BODY WASH</div>
  <div class="text volume">8.25 fl oz. / 244mL</div>

  <p class="text tagline">Our Nourishing<br>Silk Body Wash<br>will engulf you in<br>luxurious lather as it<br>gently cleanses your<br>delicate skin leaving it<br>soft as silk.</p>
  <p class="text directions">Directions: Apply to skin while damp with sponge or wash cloth. Rinse well.</p>
  <p class="text warnings">WARNINGS/CAUTIONS:<br>For external use only. Avoid<br>contact with eyes.</p>
  <p class="text claim">NOT TESTED ON ANIMALS</p>
  <p class="text ingredients"><strong>INGREDIENTS:</strong> purified water, sodium olefin sulfonate (plant source), organic aloe barbadensis leaf juice, cocamidopropylbetaine (plant source), sodium chloride (salt), kosher vegetable glycerin, tocopherol (natural vitamin E), polysorbate 20 (plant source), potassium sorbate (plant source), phenoxyethanol (mild preservative), caprylyl glycol (plant source), organic anthemisnobilis (chamomile) extract, organic calendula officinalis flower extract, xanthan gum (plant source), magnesium ascorbyl phosphate (vitamin C ester), sodium bicarbonate (baking soda), citric acid fragrance.</p>
  <p class="text company">Veltamakings<br>Bath – Body - Home</p>
  <p class="text address">Cedar Bay, FL 33000</p>
  <p class="text shop">Shop 24/7 -<br>www.veltamakings.com</p>
</main>
</body>
</html>
```